Modern corporate presentation

We need a clean, restrained company presentation in a modern Slidra style (design templates are attached for orientation). Please see the attachment for the briefing, colors and our corporate design.

content 1
Title:

VORLINQ
We connect worlds.
Digitization = increase in customer satisfaction

content 2
Animated on photo of company building (photo attached)

Text:

As Europe's leading service provider for business process outsourcing, we optimize your document management along the entire process chain of your document cycles, including physical long-term archiving after processing - efficiently, flexibly, individually and transparently!

content 3
Title: History
Overview of history as a timeline (see example design template slide 2) with dates and icons
Text:
1995
1997
2000
2016
2018
2021

content 4 or onwards
Morph transitions / individual seasons
1995 Founded by Lothar Brenning
1997 Start of ARKI@NET development
2000 real start ARKI@NET, certification GoB/S and KVR
2016 Development of Big Data + inMemory searches, first processes with AI
2018
ARKI@NET goes mobile
Expansion of the Hallstede site with a new logistics center
Launch Pagevault concept
2021 More than 400 satisfied employees

content 5
Title: Facts and Figures
Animated to morph the following texts/numbers:

family business
400 employees at different locations
Own data centers
7,500 pallet spaces
50,000 active users daily on the ARKI@NET platform
525 000 receipts per month
210 customers from all over Europe
all necessary certifications

content 6
Title: Product and service portfolio
Combine yourself...
Create animation from Tobo building blocks, which are put together, morph individually according to the order (1-3).

Module 1:
system platform
• Audit-proof archiving ARKI@NET
• Fully integrated document management
• Complete, certified KVR® integration

Module 2:
solution modules
• Digital files
• Invoice receipt workflow
ordering system
• Digital inbox
• Case management
• Info Cockpit

Module 3:

process services
• Storage
• Scanning Service
• Collection Services
• BPO Inbox
• BPO invoice receipt

content 7
Title: Good Reasons / Benefits
Trust / full-service provider for document-based business processes completely own solution
Portfolio / depiction of the entire process chain from a single source
Experience / reference projects of all sizes and industries
Employees / All services are provided by our own staff without the involvement of subcontractors

content 8
Title: The 100% Philosophy

Overview of the following 3 main points, which are highlighted individually below:

The system
Services
Privacy and Certifications
___

The system
• 100% own data center with 24x7 operation, incl. backup data center
• Certified KVR partner
• Real, completely in-house developed SaaS solution for data center operations only
• Maintenance, support and updates included
• Web-based application

Services
• Combination of man & machine
• Service level agreements, service defined in terms of time
• Penalty for non-fulfilment

Privacy and certifications:
• All common certifications
• Own compliance management
• Data protection according to GDPR

Font styles to use
Other font styles liked:
• Myrlad Pro Bold für Head und Sublines, Lucida Grande Regular für Fließtexte

Requirements
Must have
• clean and reserved, taking our corporate design into account
Nice to have
• Slidra Style, seamless transitions (similar to a glidetrack)

```html
<!DOCTYPE html>
<html lang="de">
<head>
<meta charset="utf-8">
<title>Historie</title>
<link href="https://fonts.googleapis.com/css2?family=Source+Sans+3:wght@600&family=Signika:wght@300;400&family=Open+Sans:wght@300;400;700&display=swap" rel="stylesheet">
<style>
  :root {
    --ink: #29323c;
    --text: #44464a;
    --rule: #cfcfcf;
    --sand: #d3c6a8;
    --charcoal: #3a3a3c;
    --silver: #bdbcbc;
    --stone: #8a8a89;
    --mist: #f2f2f2;
    --mist-edge: #c4c4c4;
    --steel: #6b8799;
    --icon: #b8a886;
    --disc: #f0f0f0;
    --footer: #29323c;
  }
  * { margin: 0; padding: 0; box-sizing: border-box; }
  html, body { width: 1200px; height: 675px; overflow: hidden; background: #fff; }
  .slide { position: relative; width: 1200px; height: 675px; background: #fff; }
  .slide-title {
    position: absolute; top: 48px; left: 0; width: 1200px; text-align: center;
    font-family: "Source Sans 3", sans-serif; font-weight: 600; font-size: 33px;
    color: var(--ink); letter-spacing: -0.5px;
  }
  .title-rule { position: absolute; top: 92px; left: 116px; width: 968px; height: 1px; background: var(--rule); }
  .timeline { position: absolute; inset: 0; }
  .milestone-text {
    position: absolute; font-family: "Signika", sans-serif; font-weight: 300;
    font-size: 15px; line-height: 22px; color: var(--text);
  }
  .milestone-text.align-right { text-align: right; }
  .milestone-text p + p { margin-top: 6px; }
  .year { font-family: "Open Sans", sans-serif; font-weight: 700; font-size: 19px; }
  .footer {
    position: absolute; left: 0; top: 607px; width: 1200px; height: 68px; background: var(--footer);
  }
  .brand {
    position: absolute; left: 119px; top: 22px;
    font-family: "Open Sans", sans-serif; font-weight: 300; font-size: 21px; color: #e6e6e6;
    letter-spacing: 0.5px; line-height: 1;
  }
  .deck-title {
    position: absolute; right: 164px; top: 25px; font-family: "Open Sans", sans-serif;
    font-size: 14px; letter-spacing: 1.2px; color: #fff;
  }
  .footer-divider { position: absolute; left: 1049px; top: 17px; width: 1px; height: 51px; background: #fff; }
  .page-number {
    position: absolute; left: 1060px; top: 17px; font-family: "Open Sans", sans-serif;
    font-size: 22px; color: #fff;
  }
</style>
</head>
<body>
<main class="slide">
  <h1 class="slide-title">Historie</h1>
  <div class="title-rule"></div>

  <svg class="timeline" width="1200" height="675" viewBox="0 0 1200 675" aria-label="Zeitstrahl 1995 bis 2021">
    <g class="chevrons">
      <polygon points="126,323 270,323 276,342 270,361 126,361 132,342" fill="var(--sand)"/>
      <polygon points="286,323 430,323 436,342 430,361 286,361 292,342" fill="var(--charcoal)"/>
      <polygon points="446,323 590,323 596,342 590,361 446,361 452,342" fill="var(--silver)"/>
      <polygon points="607,323 751,323 757,342 751,361 607,361 613,342" fill="var(--stone)"/>
      <polygon points="767.5,323.5 911,323.5 916.5,342 911,360.5 767.5,360.5 773,342" fill="var(--mist)" stroke="var(--mist-edge)" stroke-width="1"/>
      <polygon points="927,323 1071,323 1077,342 1071,361 927,361 933,342" fill="var(--steel)"/>
    </g>
    <g class="year" text-anchor="middle">
      <text x="201" y="349" fill="var(--charcoal)">1995</text>
      <text x="361" y="349" fill="#fff">1997</text>
      <text x="521" y="349" fill="var(--charcoal)">2000</text>
      <text x="681" y="349" fill="#fff">2016</text>
      <text x="837" y="349" fill="var(--charcoal)">2018</text>
      <text x="1002" y="349" fill="#fff">2021</text>
    </g>

    <g fill="none" stroke-width="2">
      <path d="M327,234 A34,34 0 1 1 361,268 L361,323" stroke="var(--charcoal)"/>
      <path d="M650,234 A34,34 0 1 1 684,268 L684,323" stroke="var(--stone)"/>
      <path d="M968,234 A34,34 0 1 1 1002,268 L1002,323" stroke="var(--steel)"/>
    </g>
    <g fill="none" stroke-width="2">
      <path d="M201,361 L201,416 A34,34 0 1 0 235,450" stroke="var(--sand)"/>
      <path d="M479,361 L479,416 A34,34 0 1 0 513,450" stroke="var(--silver)"/>
      <path d="M799,352 L799,416 A34,34 0 1 0 833,450" stroke="#d4d4d4"/>
    </g>

    <g fill="var(--disc)">
      <circle cx="361" cy="234" r="27"/>
      <circle cx="684" cy="234" r="27"/>
      <circle cx="1002" cy="234" r="27"/>
      <circle cx="201" cy="450" r="27"/>
      <circle cx="479" cy="450" r="27"/>
      <circle cx="799" cy="450" r="27"/>
    </g>

    <g fill="none" stroke="var(--icon)" stroke-width="1.4" stroke-linecap="round" stroke-linejoin="round">
      <path d="M353,223 H369 M353,245 H369 M355,223 C355,232 367,236 367,245 M367,223 C367,232 355,236 355,245"/>
      <path d="M684,225 L695,231 L684,237 L673,231 Z M673,236 L684,242 L695,236 M673,241 L684,247 L695,241"/>
      <circle cx="997" cy="228" r="5"/>
      <path d="M987,244 C987,236 1007,236 1007,244 Z"/>
      <circle cx="1008" cy="229" r="4.2"/>
      <path d="M1005,236 C1010,235 1016,237 1016,243 H1009"/>
      <path d="M195.5,442 A11,11 0 1 0 206.5,442 M201,437 V448"/>
      <path d="M482,436 L472,452 H479 L476,465 L487,447 H480 Z"/>
      <path d="M792,457 L789,453 C795,442 804,437 811,436 C810,443 805,452 794,458 Z M795,448 L789,448 L786,452 L790,453 M799,452 L799,458 L795,461 L794,457"/>
      <circle cx="803" cy="444" r="2"/>
      <path d="M789,458 L786,461"/>
    </g>
  </svg>

  <div class="milestone-text align-right" style="right:893px; top:212px;">
    <p>Start Entwicklung<br>ARKI@NET</p>
  </div>
  <div class="milestone-text align-right" style="right:568px; top:205px;">
    <p>Entwicklung Big Data +<br>inMemory Suchen,<br>Erste Prozesse mit KI</p>
  </div>
  <div class="milestone-text align-right" style="right:252px; top:213px;">
    <p>Mehr als 400<br>zufriedene Mitarbeiter</p>
  </div>
  <div class="milestone-text" style="left:253px; top:429px;">
    <p>Gegründet von<br>Lothar Brenning</p>
  </div>
  <div class="milestone-text" style="left:532px; top:416px;">
    <p>Echtstart ARKI@NET,<br>Zertifizierung GoB/S<br>und KVR</p>
  </div>
  <div class="milestone-text" style="left:851px; top:406px; line-height:19px;">
    <p>ARKI@NET wird mobil;</p>
    <p>Erweiterung des Standortes Hallstede<br>durch neues Logistikzentrum;</p>
    <p>Start Pagevault Konzept</p>
  </div>

  <footer class="footer">
    <div class="brand">VORLINQ</div>
    <div class="deck-title">PRESENTATION TITLE</div>
    <div class="footer-divider"></div>
    <div class="page-number">02</div>
  </footer>
</main>
</body>
</html>
```